Keepers of the Salt Roads book cover

My goal is to choose a submission ready cover for my self-published book. I am looking for an illustrative design that coordinates with the mood of the book, and with current market expectations.

Attached for context are three prior drafts of the cover. My desire is for something more illustrative (like the first one) than obvious AI, like the other two. The story takes place in a fictional town in the Arizona desert. The landscape is a big part of the story. So I would like the mood and color palette to reflect the desert. Reflect; not be a photorealistic depiction of desert. It need not portray the desert explicitly at all, if the design can invoke it. The book does have a fantasy story, but I do not want a "fantasy book" cover. Something more contemporary in design and font choices.

For example, this cover invokes the sea: https://www.bookvarnel.example/item/47213

This one invokes a forest at night: https://www.bookvarnel.example/item/58324

And this one a different take on the sea: https://www.bookvarnel.example/item/69435

(By the way, my book with its current cover, which I hate, is at:)
https://www.bookvarnel.example/item/70546

Target Market(s)

25-80 year old, professional females.

Font styles to use
Other font styles liked:
• For the Author Name, use upper and lower case (i.e., Dale Worthen), with Abadi font, if possible. In the title, make "of the" lower case.

Requirements
Must have
• Copper Wren logo on the spine, with the words "Copper Wren" beneath it.

```html
<!DOCTYPE html>
<html lang="en">
<head>
<meta charset="utf-8">
<title>Keepers of the Salt Roads – Cover Spread</title>
<link rel="stylesheet" href="https://fonts.googleapis.com/css2?family=Encode+Sans+Condensed:wght@300;400&family=Encode+Sans+Semi+Condensed:wght@500&family=Josefin+Sans:wght@700&display=swap">
<style>
  :root {
    --page-bg: #ffffff;
    --sky-violet: #3c1848;
    --sky-magenta: #8a2c50;
    --sunset-orange: #e8622a;
    --sunset-amber: #f28a34;
    --sun-core: #fbe27a;
    --ridge-rose: #9a3448;
    --valley-plum: #5a1e40;
    --ground-dark: #2a0e26;
    --ink-light: #ffffff;
    --box-white: #ffffff;
  }
  * { box-sizing: border-box; margin: 0; padding: 0; }
  html, body {
    width: 864px; height: 1200px; overflow: hidden;
    background: var(--page-bg);
  }
  .canvas { position: relative; width: 864px; height: 1200px; }

  .spread {
    position: absolute; left: 0; top: 283px;
    width: 864px; height: 634px; overflow: hidden;
    color: var(--ink-light);
  }
  .artwork {
    position: absolute; inset: 0;
    background:
      radial-gradient(circle at 709px 226px, var(--sun-core) 0 24px, rgba(251,226,122,.7) 30px, rgba(242,138,52,.55) 70px, rgba(232,98,42,0) 190px),
      radial-gradient(ellipse 420px 200px at 640px 180px, rgba(242,138,52,.75), rgba(232,98,42,0) 100%),
      radial-gradient(ellipse 380px 180px at 200px 140px, rgba(200,70,60,.45), rgba(200,70,60,0) 100%),
      linear-gradient(180deg,
        var(--sky-violet) 0%,
        var(--sky-magenta) 12%,
        var(--sunset-orange) 30%,
        var(--ridge-rose) 48%,
        var(--valley-plum) 70%,
        var(--ground-dark) 100%);
  }
  .artwork::after {
    content: ""; position: absolute; left: 0; top: 0; width: 413px; height: 100%;
    background: linear-gradient(90deg, rgba(42,14,38,.4), rgba(42,14,38,.18));
  }

  /* Back cover */
  .back { position: absolute; left: 0; top: 0; width: 413px; height: 100%; }
  .title-lockup { position: absolute; text-align: center; }
  .title-word {
    display: block;
    font-family: "Josefin Sans", sans-serif; font-weight: 700;
    color: transparent; -webkit-text-stroke: 1.3px var(--ink-light);
    line-height: 1; letter-spacing: .02em;
  }
  .title-of {
    display: flex; align-items: center; justify-content: center; gap: 12px;
    font-family: "Encode Sans Condensed", sans-serif; font-weight: 400;
    line-height: 1;
  }
  .title-of::before, .title-of::after {
    content: ""; height: 1.5px; background: var(--ink-light);
  }
  .back .title-lockup { left: 30px; top: 32px; width: 360px; }
  .back .title-word { font-size: 40px; }
  .back .title-of { font-size: 18px; margin: 4px 0 6px; }
  .back .title-of::before, .back .title-of::after { width: 44px; }

  .blurb {
    position: absolute; left: 36px; top: 152px; width: 344px;
    font-family: "Encode Sans Condensed", sans-serif; font-weight: 300;
    font-size: 11.4px; line-height: 15.8px; text-align: justify;
    text-align-last: center;
  }
  .blurb p + p { margin-top: 15.8px; }

  .barcode-space {
    position: absolute; left: 261px; top: 525px;
    width: 137px; height: 83px; background: var(--box-white);
  }

  /* Spine */
  .spine { position: absolute; left: 413px; top: 0; width: 37px; height: 100%; }
  .spine-title {
    position: absolute; left: 6px; top: 36px;
    writing-mode: vertical-rl; white-space: nowrap;
    font-size: 21px; line-height: 1;
  }
  .spine-title .caps {
    font-family: "Josefin Sans", sans-serif; font-weight: 700;
    color: transparent; -webkit-text-stroke: .8px var(--ink-light);
    letter-spacing: .04em;
  }
  .spine-title .small {
    font-family: "Encode Sans Condensed", sans-serif; font-weight: 400;
    font-size: 17px; margin: 6px 0;
  }
  .spine-author {
    position: absolute; left: 8px; top: 388px;
    writing-mode: vertical-rl; white-space: nowrap;
    font-family: "Encode Sans Semi Condensed", sans-serif; font-weight: 500;
    font-size: 17.5px;
  }
  .imprint {
    position: absolute; left: -4px; top: 546px; width: 45px;
    display: flex; flex-direction: column; align-items: center; gap: 5px;
  }
  .imprint-mark {
    width: 30px; height: 30px; border-radius: 50%;
    border: 1.5px solid var(--ink-light);
  }
  .imprint-name {
    font-family: "Encode Sans Condensed", sans-serif; font-weight: 400;
    font-size: 8px; white-space: nowrap;
  }

  /* Front cover */
  .front { position: absolute; left: 450px; top: 0; width: 414px; height: 100%; }
  .front-author {
    position: absolute; left: 0; top: 30px; width: 100%; text-align: center;
    font-family: "Encode Sans Semi Condensed", sans-serif; font-weight: 500;
    font-size: 35px; line-height: 1;
  }
  .front .title-lockup { left: 12px; top: 446px; width: 390px; }
  .front .title-word { font-size: 54px; }
  .front .title-of { font-size: 27px; margin: 6px 0 8px; gap: 16px; }
  .front .title-of::before, .front .title-of::after { width: 72px; }
</style>
</head>
<body>
<main class="canvas">
  <section class="spread" aria-label="Full wraparound cover for Keepers of the Salt Roads">
    <div class="artwork" role="img" aria-label="Illustrated Arizona desert at sunset: glowing sun over red mountain ridges, saguaro cacti and a trail through a plum-toned valley, stretching across back, spine and front"></div>

    <div class="back">
      <h2 class="title-lockup">
        <span class="title-word">KEEPERS</span>
        <span class="title-of">of the</span>
        <span class="title-word">SALT ROADS</span>
      </h2>
      <div class="blurb">
        <p>Lucas Grant, a sharp-minded but skeptical scientist, arrives in Redstone, Arizona, with one goal: to debunk the age-old myths surrounding ley lines. But what begins as a methodical investigation into unexplained energy readings quickly spirals into a journey fraught with mystery, danger, and an unsettling clash between science and the unexplainable.</p>
        <p>As Lucas uncovers bizarre data he can’t rationalize, his path crosses with Sierra Castillo, a fiercely independent artist who draws her strength from the desert’s ancient rhythms. Deeply connected to the land and its hidden energies, Sierra’s insights defy Lucas’s logic and force him to confront truths far older—and more powerful—than anything in his textbooks.</p>
        <p>Together, they delve into the ley lines’ enigmatic power, uncovering a story woven with mystic lore, ecological activism, and a battle for the heart of a community threatened by corporate greed. As the pulse of the Earth calls to Lucas, he must decide: will he cling to the safety of skepticism, or embrace the wonder and responsibility of a force that could rewrite everything he thought he knew?</p>
        <p>With breathtaking desert landscapes, unforgettable characters, and a seamless blend of science and magic, Keepers of the Salt Roads invites readers on an exhilarating quest for truth. Can Lucas and Sierra save Redstone’s future—or will the ley lines’ secrets remain buried forever?</p>
      </div>
      <div class="barcode-space" aria-hidden="true"></div>
    </div>

    <div class="spine">
      <p class="spine-title"><span class="caps">KEEPERS</span><span class="small"> of the </span><span class="caps">SALT ROADS</span></p>
      <p class="spine-author">Dale Worthen</p>
      <div class="imprint">
        <span class="imprint-mark" aria-hidden="true"></span>
        <span class="imprint-name">Copper Wren</span>
      </div>
    </div>

    <div class="front">
      <p class="front-author">Dale Worthen</p>
      <h1 class="title-lockup">
        <span class="title-word">KEEPERS</span>
        <span class="title-of">of the</span>
        <span class="title-word">SALT ROADS</span>
      </h1>
    </div>
  </section>
</main>
</body>
</html>
```